Article/Flyer - Reservation of Rights

We would like an article that we normally produce through illustrator in a pdf format to be placed in a Word format. We have provided a sample article/flyer of our normal distribution style. We would like the outcome to be in WORD format

```html
<!DOCTYPE html>
<html lang="en">
<head>
<meta charset="utf-8">
<title>Reservation of Rights Letter – Larkin &amp; Company</title>
<link href="https://fonts.googleapis.com/css2?family=Arimo:wght@400;700&family=Alegreya:wght@400&display=swap" rel="stylesheet">
<style>
  :root {
    --brand-red: #8b2331;
    --ink: #1f1f1f;
    --slate-blue: #6f8ea3;
    --white: #ffffff;
  }
  * { margin: 0; padding: 0; box-sizing: border-box; }
  html, body { width: 927px; height: 1200px; overflow: hidden; background: var(--white); }
  .page { position: relative; width: 927px; height: 1200px; overflow: hidden; font-family: "Arimo", Arial, sans-serif; color: var(--ink); }

  .masthead { position: absolute; left: 43px; top: 43px; width: 841px; height: 289px; }
  .masthead-art { position: absolute; inset: 0; width: 100%; height: 100%; }
  .brand { position: absolute; left: 75px; top: 32px; color: #222; font-family: "Arimo", Arial, sans-serif; font-weight: 400; }
  .brand-name { font-size: 34px; line-height: 1; }
  .brand-tagline { font-size: 13px; margin-top: 10px; }
  .brand-legal { font-size: 10.5px; margin-top: 6px; }

  .intro-band { position: absolute; left: 43px; top: 346px; width: 841px; height: 124px; background: var(--brand-red); color: var(--white); padding: 17px 30px 0 19px; font-size: 22.4px; line-height: 22.8px; }

  .column { position: absolute; top: 496px; width: 406px; font-size: 13.2px; line-height: 15.2px; }
  .column-left { left: 43px; width: 404px; }
  .column-right { left: 480px; width: 406px; }
  .column h2 { color: var(--brand-red); font-size: 13.2px; font-weight: 700; line-height: 15.2px; text-transform: uppercase; }
  .column p { margin-bottom: 11.8px; }

  .promo { position: absolute; left: 481px; width: 404px; }
  .promo-pitch { top: 870px; height: 90px; background: var(--slate-blue); color: var(--white); font-family: "Alegreya", serif; font-size: 24px; line-height: 27px; text-align: center; padding-top: 4px; }
  .promo-connect { top: 968px; height: 44px; background: var(--brand-red); color: var(--white); font-family: "Alegreya", serif; font-size: 22px; line-height: 44px; text-align: center; }
  .promo-contact { top: 1018px; height: 138px; background: linear-gradient(180deg, #d6e4ef 0%, #b7cfe3 100%); }
  .office-photo { position: absolute; left: 0; top: 22px; width: 191px; height: 104px; }
  .contact-list { position: absolute; left: 205px; top: 2px; list-style: none; font-family: "Alegreya", serif; font-size: 16.5px; color: #1c1c1c; }
  .contact-list li { display: flex; align-items: center; height: 28px; }
  .contact-list .row-1 { margin-top: 4px; }
  .contact-list .row-2 { margin-top: 10px; }
  .contact-list .row-3 { margin-top: 5px; }
  .contact-list .marker { width: 18px; height: 18px; background: #3d6fa8; border-radius: 3px; margin: 0 8px 0 4px; flex: none; }
</style>
</head>
<body>
<div class="page">

  <header class="masthead">
    <svg class="masthead-art" role="img" aria-label="Photo collage: a glass office tower seen from below, a rolled insurance certificate, and three design professionals reviewing drawings at a table" viewBox="0 0 841 289" preserveAspectRatio="none">
      <defs>
        <linearGradient id="skyFade" x1="0" y1="0" x2="0" y2="1">
          <stop offset="0" stop-color="#f3f6f8"/>
          <stop offset="0.55" stop-color="#c9d8e6"/>
          <stop offset="1" stop-color="#3f5f9a"/>
        </linearGradient>
        <linearGradient id="officeFade" x1="0" y1="0" x2="1" y2="0">
          <stop offset="0" stop-color="#dfe6ec" stop-opacity="0"/>
          <stop offset="0.4" stop-color="#d8d2cb"/>
          <stop offset="1" stop-color="#b8b2ad"/>
        </linearGradient>
      </defs>
      <rect width="841" height="289" fill="url(#skyFade)"/>
      <rect x="540" width="301" height="289" fill="url(#officeFade)"/>
    </svg>
    <div class="brand">
      <div class="brand-name">Larkin &amp; Company</div>
      <div class="brand-tagline">Serving Architects, Engineers and Environmental Consultants</div>
      <div class="brand-legal">Northline Partners of Washington, LLC dba Larkin &amp; Company</div>
    </div>
  </header>

  <section class="intro-band">
    Reporting a claim or potential claim to your professional liability insurance company will trigger a fair amount of return correspondence that often creates confusion rather than clarity.&nbsp; One document that commonly falls into this category is the Reservation of Rights Letter.
  </section>

  <article class="column column-left">
    <h2>What is the Reservation of Rights Letter</h2>
    <p>The Reservation of Rights Letter is a normal part of the insurance claims process. Its purpose is to provide notification from the insurance company to the policy holder that coverage may not apply.&nbsp; While this often comes as alarming news, the Reservation of Rights Letter should not be mistaken as an outright denial -- it does not automatically mean that coverage is being or will be denied.</p>
    <p>This standard correspondence is routinely sent to comply with state laws and preserve the insurance company’s legal ability to deny some, or all, of the claim pending further investigation while the claim is ongoing and being handled by the insurance company. Failure to send the letter could be considered a waiver of their rights at a later time.</p>
    <p>Because information is vague in the early stages of a claim and often is limited to unsubstantiated allegations and a few facts, the Reservation of Rights Letter protects the insurance company’s interests to later deny coverage in whole or part based on evidence revealed during claims handling.</p>
    <h2>Interpreting the Letter</h2>
    <p>Most of the time the Reservation of Rights Letter is a generic form letter that states your insurance company is proceeding with handling your claim but reserves the right to deny coverage later on based upon any information that reveals reason to deny.</p>
    <p>Legitimate reasons an insurance company may deny coverage include when the loss occurred in relation to your retroactive date, specific exclusions in the policy language, prior knowledge of the incident, and coverage by another policy, among others.</p>
    <p>If the insurance company believes there may be reason for denial at the time the Reservation of Rights Letter is sent, it will be stated in the letter.&nbsp; For example, if the claim alleges breach of warranty, the letter will state that warranties are specifically excluded by the policy and it will include the policy language to demonstrate the exclusion.</p>
    <p>Even when specific reasons for potential coverage denial are cited, it is important to note that this is not a final verdict nor does it mean complete lack of coverage.&nbsp; Generally the insurance company is obligated to help you if any of your claims are covered by your insurance policy – there is a duty to defend.&nbsp; In cases such as the</p>
  </article>

  <article class="column column-right">
    <p>scenario above, circumstances of the claim will influence what is covered and what may be subject to exclusion.</p>
    <p>Based on investigative conclusions, the insurance company may not be obligated to pay the damages for certain types or aspects of claims.</p>
    <h2>How to Proceed</h2>
    <p>Although the intent of the Reservation of Rights Letter is to protect the insurance company’s interests, it also alerts the policy holder to the fact that some elements of a claim may not be covered and therefore allows the insured to take steps to protect its potentially uninsured interests.</p>
    <p>However, receiving the Reservation of Rights Letter and even the insurance company’s interpretation of the policy language or law that they believe points toward coverage declination does not mean that you are automatically required to accept a denial of coverage.</p>
    <p>The best thing to do upon receiving the letter is to contact your broker and work closely with them and the insurance company claims handling department to ensure the prompt and fair handling of your claim.</p>
  </article>

  <aside class="promo promo-pitch">An insurance agent who has experience<br>with large Top 100 firms as well as<br>small design firms.</aside>
  <aside class="promo promo-connect">Connect with Larkin &amp; Company</aside>
  <aside class="promo promo-contact">
    <svg class="office-photo" role="img" aria-label="Photo of the company's two-storey office building at dusk" viewBox="0 0 191 104" preserveAspectRatio="none">
      <defs>
        <linearGradient id="duskFade" x1="0" y1="0" x2="0" y2="1">
          <stop offset="0" stop-color="#aebfd0"/>
          <stop offset="0.5" stop-color="#8a4a4f"/>
          <stop offset="1" stop-color="#5a5a60"/>
        </linearGradient>
      </defs>
      <rect width="191" height="104" fill="url(#duskFade)"/>
    </svg>
    <ul class="contact-list">
      <li class="web">www.larkinandcompany.com</li>
      <li class="row-1"><span class="marker"></span>/LarkinAndCompany</li>
      <li class="row-2"><span class="marker"></span>/RLLarkinAndCompany</li>
      <li class="row-3"><span class="marker"></span>/LarkinAndCompany</li>
    </ul>
  </aside>

</div>
</body>
</html>
```